Landing Page concept design for lead generation . Design only first, likely landing page development thereafter. Please refer to the instructions uploaded. Use colours to best advantage. xxxxxxxxxxxxxxxxxxxxxxxxxxxxxxxxxxxxxxxxxxxxxxxxxxxxxxxxxxxxxxxxxxxxxxxxxxxxxxxxxxxxxxxxxxxxxxxxxxxxxxxxxxxxxxxxxxxxxxxxxxxxxxxxxxxxxxxxxxxxxxxxxxxxxx

Target Market(s)

High end Kitchen Design

Industry/Entity Type

Kitchen

Number of Pages Required

1 page

Colors
6b449b

Requirements
Must have
• See instructions
Nice to have
• See instructions
Should not have
• See instructions

```html
<!DOCTYPE html>
<html lang="en">
<head>
<meta charset="utf-8">
<title>Elite Home Group – Kitchen Price Beat</title>
<link href="https://fonts.googleapis.com/css2?family=Montserrat:wght@500;600;700;800&family=Mulish:wght@400;500;600&display=swap" rel="stylesheet">
<style>
:root{
  --purple:#6b449b;
  --purple-deep:#5a2d91;
  --ink:#1c1c1c;
  --night:#271738;
  --black:#050308;
  --white:#ffffff;
  --grey-dot:#d5d2da;
}
*{margin:0;padding:0;box-sizing:border-box}
html,body{width:1200px;height:2215px;overflow:hidden;background:var(--white)}
body{position:relative;font-family:"Mulish",sans-serif;color:var(--ink)}
.abs{position:absolute}
.center{left:0;width:1200px;text-align:center}

.hero-bg{left:0;top:0}
.brand{left:31px;top:0;width:92px;height:98px;background:var(--white);display:flex;align-items:center;justify-content:center;text-align:center;font-family:"Montserrat",sans-serif;font-weight:700;font-size:13px;line-height:1.15;color:var(--purple)}
.headline{top:193px;font-family:"Montserrat",sans-serif;font-weight:800;font-size:39px;color:var(--white);letter-spacing:.2px}
.headline .mark{background:var(--purple);padding:0 8px}
.subline{top:265px;font-family:"Mulish",sans-serif;font-weight:500;font-size:29px;color:var(--white)}
.region{top:328px;font-size:14px;font-weight:500;color:var(--white)}

.step-label{width:120px;text-align:center;font-family:"Montserrat",sans-serif;font-weight:700;color:var(--white);line-height:1}
.step-label small{display:block;font-size:18px}
.step-label b{display:block;font-size:29px;margin-top:4px}
.step-icon{width:116px;height:116px;border-radius:50%;background:var(--white);border:4px solid var(--purple-deep);display:flex;align-items:center;justify-content:center}
.step-text{width:340px;text-align:center}
.step-text h3{font-family:"Montserrat",sans-serif;font-weight:600;font-size:20px;line-height:32px;color:var(--purple-deep)}
.step-text p{font-size:15px;font-weight:600;line-height:26px;margin-top:8px}

.gallery{left:0;top:825px;width:1200px;height:391px;display:flex}
.gallery .shot-a{width:755px;background:linear-gradient(160deg,#e7e5e3 0%,#c9c5c1 45%,#6b5a52 70%,#a9a6a4 100%)}
.gallery .shot-b{flex:1;background:linear-gradient(180deg,#f3f3f3 0%,#e2e2e2 45%,#1d1b1b 50%,#3a3838 70%,#dedede 100%)}
.dots{top:1241px;left:578px;display:flex;gap:8px}
.dots span{width:9px;height:9px;border-radius:50%;background:var(--grey-dot)}
.dots span.on{background:var(--purple-deep)}

.areas-title{top:1320px;font-family:"Montserrat",sans-serif;font-weight:700;font-size:29px;line-height:42px;color:var(--purple-deep)}
.map{left:440px;top:1448px;width:270px;height:240px;border-radius:45% 40% 50% 45%;background:radial-gradient(ellipse at center,#f0eff2 0%,#fafafb 70%,#ffffff 100%)}
.area-list{list-style:none;font-size:20px;font-weight:500;line-height:42px;color:var(--ink)}

.band{left:0;top:1721px;width:1200px;height:154px;background:linear-gradient(90deg,#6a3ea0,#6e47a2 50%,#673b9c);display:flex;align-items:center;justify-content:center;font-family:"Montserrat",sans-serif;font-weight:700;font-size:29px;color:var(--white)}
.contact{left:0;top:1875px;width:1200px;height:252px;background:var(--night);color:var(--white);text-align:center}
.contact h2{position:absolute;top:30px;width:100%;font-family:"Montserrat",sans-serif;font-weight:600;font-size:20px}
.contact p{position:absolute;width:100%;font-size:15px;font-weight:500}
.footer{left:0;top:2127px;width:1200px;height:88px;background:var(--black);color:#cfcfcf;font-size:13px;display:flex;align-items:center;justify-content:center}
</style>
</head>
<body>

<svg class="abs hero-bg" width="1200" height="620" viewBox="0 0 1200 620" role="img" aria-label="Photo of a modern white and dark kitchen with marble island">
  <defs>
    <linearGradient id="heroTone" x1="0" y1="0" x2="1" y2="1">
      <stop offset="0" stop-color="#3d3b3c"/>
      <stop offset=".45" stop-color="#5e5d61"/>
      <stop offset=".75" stop-color="#2a2828"/>
      <stop offset="1" stop-color="#8d8b8f"/>
    </linearGradient>
  </defs>
  <path d="M0 0H1200V545Q604 590 0 545Z" fill="url(#heroTone)"/>
  <path d="M0 545Q604 590 1200 545" fill="none" stroke="#5a2d91" stroke-width="4"/>
  <path d="M378 566l8 6-8 6" fill="none" stroke="#5a2d91" stroke-width="3"/>
  <path d="M784 566l8 6-8 6" fill="none" stroke="#5a2d91" stroke-width="3"/>
</svg>

<div class="abs brand">Elite<br>Home<br>Group</div>

<h1 class="abs center headline">We Will <span class="mark">Beat</span> Any Written Quote By <span class="mark">10% Guaranteed</span></h1>
<p class="abs center subline">High End Kitchen Design Made Affordable</p>
<p class="abs center region">SYDNEY WIDE</p>

<div class="abs step-label" style="left:154px;top:431px"><small>STEP</small><b>01</b></div>
<div class="abs step-label" style="left:546px;top:456px"><small>STEP</small><b>02</b></div>
<div class="abs step-label" style="left:908px;top:434px"><small>STEP</small><b>03</b></div>

<div class="abs step-icon" style="left:153px;top:492px">
  <svg width="52" height="52" viewBox="0 0 52 52" fill="none" stroke="#1c1c1c" stroke-width="2">
    <rect x="4" y="6" width="44" height="30" rx="2"/><rect x="9" y="11" width="34" height="20"/>
    <path d="M14 17h12M14 22h8M20 36v6M32 36v6M14 44h24"/><path d="M34 22l6 6-3 0 2 3"/>
  </svg>
</div>
<div class="abs step-icon" style="left:546px;top:517px">
  <svg width="52" height="52" viewBox="0 0 52 52" fill="none" stroke="#1c1c1c" stroke-width="2">
    <path d="M6 8h30v36H6zM6 44l8-6M36 14l10-10 3 3-10 10"/><path d="M14 34V24l8-6 8 6v10zM20 34v-6h4v6"/>
  </svg>
</div>
<div class="abs step-icon" style="left:910px;top:492px">
  <svg width="56" height="56" viewBox="0 0 56 56" fill="none" stroke="#1c1c1c" stroke-width="2">
    <circle cx="32" cy="20" r="14"/><path d="M26 26l12-12"/><circle cx="27" cy="15" r="2.5"/><circle cx="37" cy="25" r="2.5"/>
    <path d="M4 40h8v12H4zM12 42l10-3h10l-2 5H22M30 44l12-6 4 2-16 10H12"/>
  </svg>
</div>

<div class="abs step-text" style="left:28px;top:625px">
  <h3>Click to Save<br>Website Now</h3>
  <p>Save our website and return once<br>you have your written quotes</p>
</div>
<div class="abs step-text" style="left:436px;top:650px">
  <h3>Upload Quote &amp;<br>Kitchen Plans Now</h3>
  <p>Upload your best written quote and kitchen<br>plans</p>
</div>
<div class="abs step-text" style="left:800px;top:641px">
  <h3>Send Me 10% Discount<br>Offer Now</h3>
  <p>Received no obligation offerto consider</p>
</div>

<div class="abs gallery">
  <div class="shot-a" role="img" aria-label="Photo of a bright kitchen with dark timber cabinets and window"></div>
  <div class="shot-b" role="img" aria-label="Photo of built-in black ovens in white gloss cabinetry"></div>
</div>
<div class="abs dots"><span></span><span class="on"></span><span></span></div>

<h2 class="abs center areas-title">Areas That Qualify For 10% Price Beat<br>Guarantee</h2>
<div class="abs map" role="img" aria-label="Faint dotted map of Australia"></div>
<ul class="abs area-list" style="left:360px;top:1444px">
  <li>North Shore</li><li>NothernBeaches</li><li>Eastern Suburbs</li><li>Sutherland Shire</li>
</ul>
<ul class="abs area-list" style="left:658px;top:1439px">
  <li>St George Area</li><li>Inner West</li><li>Central Sydney</li><li>Western Sydney</li><li>Penrith</li>
</ul>

<div class="abs band" role="img" aria-label="Purple tinted kitchen photo banner"><span>Luxurious Kitchens Made Affordably</span></div>

<section class="abs contact">
  <h2>CONTACT US</h2>
  <p style="top:99px">Email: offers@elitehomekitchens.com.au</p>
  <p style="top:126px">14 Harbour Lane, Redfern NSW 2016</p>
  <p style="top:161px">Mob: 0400 123 456</p>
</section>

<footer class="abs footer">Copyright © 2019 elitehomekitchens.com.au</footer>

</body>
</html>
```